Menu Design Project for new restauranct concept

Design menu for new restaurant concept called Juniper's Burgers & Dogs. Logo is attached.

Industry/Entity Type

Restaurant

Requirements
Must have
• Menu items and pricing:

Burgers
Snack Burger $3.49
Snack Cheeseburger $3.99
Juniper's signature Burger $4.99
Juniper's signature Cheeseburger $5.49
Burger toppings: bacon, lettuce, tomato, onion, pickle, grilled onions, grilled mushrooms, grilled green peppers, jalapeƱo peppers.

Dogs
Hot Dog $2.99
Bacon Cheese Hot Dog $3.99
Slaw Dog $3.99
Kraut Dog $3.49
Chili Dog $3.99 with or with out cheese
Hot dogs are 100% beef

Other
Grilled Chicken Sandwich $5.99
Grilled Chicken Sandwich with cheese $6.49
(Same toppings as burgers)

French Fries $1.99

Loaded Potatos
The Plain Tater: $4.99 choose from: butter, sour cream, cheese, chives
The Garden Tater: $5.99 choose from: the Basic plus, broccoli & cheese, grilled mushrooms, onions, & peppers
The Rancher Tater: $6.99 choose from the Basic/Veggie plus: grilled chicken, chili, Philly cheesesteak, pulled pork.

Drinks
32oz. Drink $1.88
20oz. Drink $1.69

attached logo.
Nice to have
• love to incorporate the woodgrain backgound. It makes the logo look most like a cattle brand, which we like.

```html
<!DOCTYPE html>
<html lang="en">
<head>
<meta charset="utf-8">
<title>Juniper's Burgers &amp; Dogs — Menu</title>
<link rel="stylesheet" href="https://fonts.googleapis.com/css2?family=Alfa+Slab+One&family=Roboto+Slab:wght@700;900&family=Dancing+Script:wght@500&display=swap">
<style>
  :root {
    --stage: #e9e6df;
    --wood-light: #8a8580;
    --wood-mid: #6b6661;
    --wood-dark: #4a4541;
    --plank-line: rgba(30, 26, 22, 0.55);
    --title-tan: #d9b184;
    --title-shadow: #5a3a1c;
    --brand-ink: #161413;
    --parchment-light: #ecd6a6;
    --parchment-mid: #dcbd84;
    --parchment-dark: #b98d4f;
    --ink: #2a2118;
    --horseshoe: #8a5230;
    --rope: #b89c72;
  }
  * { box-sizing: border-box; margin: 0; padding: 0; }
  html, body { width: 1200px; height: 1000px; overflow: hidden; }
  body { background: var(--stage); position: relative; }

  .menu-card {
    position: absolute; left: 230px; top: 20px;
    width: 740px; height: 960px; overflow: hidden;
    background: linear-gradient(180deg, var(--wood-light), var(--wood-mid) 60%, var(--wood-dark));
    box-shadow: 0 10px 30px rgba(0,0,0,0.25);
  }
  .wood-planks { position: absolute; inset: 0; }

  .menu-title {
    position: absolute; left: 60px; top: 40px;
    font-family: "Alfa Slab One", serif; font-size: 76px; line-height: 1;
    color: var(--title-tan); text-shadow: 3px 4px 0 var(--title-shadow);
    transform: rotate(-4deg);
  }
  .brand {
    position: absolute; right: 40px; top: 50px; width: 300px;
    display: flex; flex-direction: column; align-items: center; gap: 10px;
  }
  .brand-mark { width: 60px; height: 60px; border-radius: 50%; background: var(--brand-ink); }
  .brand-name {
    font-family: "Roboto Slab", serif; font-weight: 900; font-size: 30px;
    color: var(--brand-ink); text-align: center; line-height: 1.15; text-transform: uppercase;
  }

  .parchment {
    position: absolute; left: 30px; top: 290px; right: 0; bottom: 0;
    background: radial-gradient(ellipse at 50% 45%, var(--parchment-light), var(--parchment-mid) 70%, var(--parchment-dark));
  }
  .horseshoe {
    position: absolute; left: 40px; top: 195px; width: 200px; height: 100px;
    border-radius: 100px 100px 0 0; background: var(--horseshoe);
  }
  .rope {
    position: absolute; right: 40px; bottom: 0; width: 230px; height: 90px;
    border-radius: 115px 115px 0 0; background: var(--rope);
  }

  .menu-section { position: absolute; color: var(--ink); }
  .section-heading {
    font-family: "Roboto Slab", serif; font-weight: 700; font-size: 19px;
    padding: 0 0 3px 14px; border-bottom: 2px solid var(--ink); width: 170px; margin-bottom: 10px;
  }
  .menu-item {
    display: flex; align-items: baseline;
    font-family: "Dancing Script", cursive; font-size: 17px; line-height: 1.55; padding-left: 14px;
  }
  .item-name { white-space: nowrap; }
  .item-leader { flex: 1; border-bottom: 2px dotted var(--ink); margin: 0 6px; transform: translateY(-4px); }
  .item-price { white-space: nowrap; }
  .menu-note {
    font-family: "Dancing Script", cursive; font-size: 13px; line-height: 1.5; padding-left: 8px;
  }
  .menu-note.large { font-size: 16px; margin-top: 8px; }

  .burgers { left: 70px; top: 360px; width: 290px; }
  .other { left: 70px; top: 610px; width: 290px; }
  .drinks { left: 70px; top: 800px; width: 280px; }
  .dogs { left: 400px; top: 360px; width: 300px; }
  .potatoes { left: 390px; top: 610px; width: 310px; }
  .potatoes .section-heading { width: 200px; }
</style>
</head>
<body>
  <main class="menu-card">
    <svg class="wood-planks" width="740" height="960" viewBox="0 0 740 960" aria-hidden="true">
      <g stroke="var(--plank-line)" stroke-width="2">
        <line x1="0" y1="60" x2="740" y2="110"/>
        <line x1="0" y1="130" x2="740" y2="180"/>
        <line x1="0" y1="200" x2="740" y2="250"/>
        <line x1="0" y1="270" x2="740" y2="320"/>
        <line x1="20" y1="300" x2="20" y2="960"/>
      </g>
    </svg>

    <h1 class="menu-title">Menu</h1>

    <div class="brand">
      <span class="brand-mark" aria-hidden="true"></span>
      <p class="brand-name">Juniper's<br>Burgers &amp; Dogs</p>
    </div>

    <div class="parchment" role="img" aria-label="Aged torn parchment sheet"></div>
    <div class="horseshoe" role="img" aria-label="Rusty horseshoe"></div>
    <div class="rope" role="img" aria-label="Coiled lasso rope"></div>

    <section class="menu-section burgers">
      <h2 class="section-heading">Burgers</h2>
      <p class="menu-item"><span class="item-name">Snack Burger</span><span class="item-leader"></span><span class="item-price">$ 3.49</span></p>
      <p class="menu-item"><span class="item-name">Snack Cheeseburger</span><span class="item-leader"></span><span class="item-price">$ 3.99</span></p>
      <p class="menu-item"><span class="item-name">Juniper's signature Burger</span><span class="item-leader"></span><span class="item-price">$ 4.99</span></p>
      <p class="menu-item"><span class="item-name">Juniper's signature Cheeseburger</span><span class="item-leader"></span><span class="item-price">$ 5.49</span></p>
      <p class="menu-note">Burger toppings: bacon, lettuce, tomato, onion, pickle, grilled onions, grilled mushrooms, grilled green peppers, jalapeño peppers.</p>
    </section>

    <section class="menu-section other">
      <h2 class="section-heading">Other</h2>
      <p class="menu-item"><span class="item-name">Grilled Chicken Sandwich</span><span class="item-leader"></span><span class="item-price">$ 5.99</span></p>
      <p class="menu-item"><span class="item-name">Grilled Chicken Sandwich<br>with cheese</span><span class="item-leader"></span><span class="item-price">$ 6.49</span></p>
      <p class="menu-note">(Same toppings as burgers)</p>
      <p class="menu-item"><span class="item-name">French Fries</span><span class="item-leader"></span><span class="item-price">$ 1.99</span></p>
    </section>

    <section class="menu-section drinks">
      <h2 class="section-heading">Drinks</h2>
      <p class="menu-item"><span class="item-name">32 oz. Drink</span><span class="item-leader"></span><span class="item-price">$ 1.88</span></p>
      <p class="menu-item"><span class="item-name">20 oz. Drink</span><span class="item-leader"></span><span class="item-price">$ 1.69</span></p>
    </section>

    <section class="menu-section dogs">
      <h2 class="section-heading">Dogs</h2>
      <p class="menu-item"><span class="item-name">Hot Dog</span><span class="item-leader"></span><span class="item-price">$ 2.99</span></p>
      <p class="menu-item"><span class="item-name">Bacon Cheese Hot Dog</span><span class="item-leader"></span><span class="item-price">$ 3.99</span></p>
      <p class="menu-item"><span class="item-name">Slaw Dog</span><span class="item-leader"></span><span class="item-price">$ 3.99</span></p>
      <p class="menu-item"><span class="item-name">Kraut Dog</span><span class="item-leader"></span><span class="item-price">$ 3.49</span></p>
      <p class="menu-item"><span class="item-name">Chili Dog</span><span class="item-leader"></span><span class="item-price">$ 3.99</span></p>
      <p class="menu-note">With or with out cheese</p>
      <p class="menu-note large">Hot dogs are 100% beef</p>
    </section>

    <section class="menu-section potatoes">
      <h2 class="section-heading">Loaded Potatos</h2>
      <p class="menu-item"><span class="item-name">The Plain Tater</span><span class="item-leader"></span><span class="item-price">$ 4.99</span></p>
      <p class="menu-note">choose from: butter, sour cream, cheese, chives</p>
      <p class="menu-item"><span class="item-name">The Garden Tater</span><span class="item-leader"></span><span class="item-price">$ 5.99</span></p>
      <p class="menu-note">choose from: the Basic plus, broccoli &amp; cheese, grilled mushrooms, onions, &amp; peppers</p>
      <p class="menu-item"><span class="item-name">The Rancher Tater</span><span class="item-leader"></span><span class="item-price">$ 6.99</span></p>
      <p class="menu-note">choose from the Basic/Veggie plus: grilled chicken, chili, Philly cheesesteak, pulled pork.</p>
    </section>
  </main>
</body>
</html>
```